QRDKS Updated logo business card

Can you create a new business card with our new logo? I have included a rough mockup of what our team thought of. I would need this as a background image to purchase cards via Norvellex.

Contact Information for Business Card

Title, name,

```html
<!DOCTYPE html>
<html lang="en">
<head>
<meta charset="utf-8">
<title>QRDKS Business Card</title>
<link href="https://fonts.googleapis.com/css2?family=Oswald:wght@500;600&family=Open+Sans:wght@400;600&display=swap" rel="stylesheet">
<style>
  :root {
    --page: #e9e9ec;
    --card: #ffffff;
    --maroon: #8e1b3c;
    --rose: #c23a55;
    --gold: #f2b705;
    --cream: #f3e9d6;
    --slate: #4a4a55;
    --ink: #2b2b30;
  }
  * { margin: 0; padding: 0; box-sizing: border-box; }
  html, body { width: 800px; height: 1200px; overflow: hidden; }
  body { background: var(--page); font-family: "Open Sans", Arial, sans-serif; color: var(--ink); position: relative; }

  .card {
    position: absolute; left: 80px; width: 640px; height: 366px;
    background: var(--card); overflow: hidden;
    box-shadow: 0 8px 24px rgba(0,0,0,0.12);
  }
  .card-front { top: 194px; }
  .card-back { top: 640px; }

  .stripe { position: absolute; }
  .stripe-cream { background: var(--cream); }
  .stripe-rose { background: var(--rose); }
  .stripe-gold { background: var(--gold); }
  .stripe-pattern { background: var(--slate); }
  .band-maroon { background: var(--maroon); }

  /* front */
  .card-front .stripe-cream { left: 30px; top: 0; width: 60px; height: 100%; }
  .card-front .stripe-rose { left: 90px; top: 0; width: 22px; height: 100%; }
  .card-front .stripe-pattern { left: 112px; top: 0; width: 22px; height: 70px; }
  .card-front .stripe-gold { left: 134px; top: 0; width: 22px; height: 100%; }
  .card-front .band-maroon { position: absolute; left: 112px; top: 70px; width: 528px; height: 62px; }

  .holder-name {
    position: absolute; left: 196px; top: 76px;
    font-family: "Oswald", "Arial Narrow", sans-serif; font-weight: 600;
    font-size: 36px; letter-spacing: 1px; color: #fff; line-height: 50px;
  }
  .holder-position {
    position: absolute; left: 196px; top: 142px;
    font-family: "Oswald", "Arial Narrow", sans-serif; font-weight: 500;
    font-size: 17px; letter-spacing: 1.5px; color: var(--ink);
  }
  .contact-list { position: absolute; left: 196px; top: 190px; list-style: none; }
  .contact-item { display: flex; align-items: center; height: 34px; font-size: 14px; color: var(--ink); }
  .contact-icon { width: 22px; height: 22px; margin-right: 12px; flex: none; }

  /* back */
  .card-back .stripe-pattern { left: 430px; top: 0; width: 22px; height: 258px; }
  .card-back .stripe-gold { left: 460px; top: 0; width: 26px; height: 100%; }
  .card-back .stripe-cream { left: 494px; top: 0; width: 64px; height: 100%; }
  .card-back .band-maroon { position: absolute; left: 0; top: 258px; width: 640px; height: 44px; }

  .brand-name {
    position: absolute; left: 60px; top: 92px;
    font-family: "Oswald", "Arial Narrow", sans-serif; font-weight: 600;
    font-size: 58px; letter-spacing: 3px; color: var(--maroon); line-height: 1;
  }
  .brand-address {
    position: absolute; left: 62px; top: 180px;
    font-size: 12px; line-height: 18px; color: var(--ink);
  }
</style>
</head>
<body>

<section class="card card-front" aria-label="Business card front">
  <div class="stripe stripe-cream"></div>
  <div class="stripe stripe-rose"></div>
  <div class="stripe stripe-gold"></div>
  <div class="stripe stripe-pattern" role="img" aria-label="Flag-inspired checker pattern"></div>
  <div class="band-maroon"></div>
  <h1 class="holder-name">YOUR NAME</h1>
  <p class="holder-position">POSITION</p>
  <ul class="contact-list">
    <li class="contact-item">
      <svg class="contact-icon" viewBox="0 0 22 22"><circle cx="11" cy="11" r="11" fill="#2b2b30"/><rect x="6" y="7.5" width="10" height="7" fill="none" stroke="#fff" stroke-width="1.3"/><path d="M6 7.5l5 4 5-4" fill="none" stroke="#fff" stroke-width="1.3"/></svg>
      name@thecompany.com
    </li>
    <li class="contact-item">
      <svg class="contact-icon" viewBox="0 0 22 22"><circle cx="11" cy="11" r="11" fill="#2b2b30"/><circle cx="11" cy="11" r="5" fill="none" stroke="#fff" stroke-width="1.3"/><path d="M6 11h10M11 6c-2.5 3-2.5 7 0 10M11 6c2.5 3 2.5 7 0 10" fill="none" stroke="#fff" stroke-width="1.1"/></svg>
      yourwebaddress.com
    </li>
    <li class="contact-item">
      <svg class="contact-icon" viewBox="0 0 22 22"><circle cx="11" cy="11" r="11" fill="#2b2b30"/><path d="M8 6.5l2 2.5-1.2 1.3c.7 1.4 1.6 2.3 2.9 2.9l1.3-1.2 2.5 2-1 1.5c-3.8-.2-7.4-3.8-7.6-7.6z" fill="#fff"/></svg>
      (555) 456-7890
    </li>
    <li class="contact-item">
      <svg class="contact-icon" viewBox="0 0 22 22"><circle cx="11" cy="11" r="11" fill="#2b2b30"/><rect x="6.5" y="6.5" width="9" height="9" rx="1.5" fill="none" stroke="#fff" stroke-width="1.3"/></svg>
      yourlinkedinaddress
    </li>
  </ul>
</section>

<section class="card card-back" aria-label="Business card back">
  <div class="stripe stripe-pattern" role="img" aria-label="Flag-inspired checker pattern"></div>
  <div class="band-maroon"></div>
  <div class="stripe stripe-gold"></div>
  <div class="stripe stripe-cream"></div>
  <p class="brand-name">QRDKS</p>
  <address class="brand-address" style="font-style:normal">
    1175 Harrowgate Lane Suite B<br>
    Ashford Vale, Maryland 21990
  </address>
</section>

</body>
</html>
```